Law Firm Stationery Design - Traditional Meets Intuitive

Looking for a modern, yet classic, law firm stationery design. Simplicity is desired, but great ideas are encouraged. See attachment for company information. We utilize a variety of non-traditional legal tools to bring a different perspective to each of our client's particular situation. Final design should communicate classic values with intuitive, unique solutions.

Industry/Entity Type

Law Firm

Requirements
Should not have
• - No typical legal icons
• - No Tag Line!
• - DO NOT WANT WHAT WE ALREADY HAVE

```html
<!DOCTYPE html>
<html lang="en">
<head>
<meta charset="utf-8">
<title>Veridian Law – Business Card</title>
<link rel="stylesheet" href="https://fonts.googleapis.com/css2?family=Old+Standard+TT:wght@400;700&family=Arimo:wght@400;700&display=swap">
<style>
  :root {
    --page: #e9e7e3;
    --ink: #111111;
    --card-white: #ffffff;
    --band-black: #141414;
    --accent-blue: #1d6fb0;
    --accent-blue-dark: #155a92;
    --text-light: #f2f2f2;
    --text-grey: #cfcfcf;
    --serif: "Old Standard TT", Georgia, serif;
    --sans: "Arimo", Arial, sans-serif;
  }
  * { box-sizing: border-box; margin: 0; padding: 0; }
  html, body {
    width: 1200px; height: 950px; overflow: hidden;
    background: var(--page);
  }
  .sheet { position: relative; width: 1200px; height: 950px; }

  .card {
    position: absolute; left: 250px; width: 700px; height: 400px;
    overflow: hidden; box-shadow: 0 6px 18px rgba(0,0,0,.18);
  }

  .wordmark {
    font-family: var(--serif); font-weight: 400; font-size: 64px;
    line-height: 1; letter-spacing: 1px; white-space: nowrap;
  }

  /* Back side */
  .card--back {
    top: 50px;
    background: linear-gradient(100deg, #050505 0%, #141414 55%, #2a2a2a 70%, #0a0a0a 85%, #050505 100%);
    text-align: center;
  }
  .card--back .wordmark { margin-top: 140px; color: #e6e6e6; }
  .card--back .website {
    margin-top: 56px; font-family: var(--sans); font-size: 17px;
    letter-spacing: 6px; color: var(--text-grey);
  }

  /* Front side */
  .card--front { top: 500px; background: var(--card-white); color: var(--ink); }
  .front-brand { position: absolute; top: 48px; width: 100%; text-align: center; }
  .person { position: absolute; top: 150px; width: 100%; text-align: center; }
  .person-name { font-family: var(--sans); font-weight: 700; font-size: 22px; letter-spacing: .5px; }
  .person-title { font-family: var(--sans); font-size: 19px; color: var(--accent-blue); margin-top: 2px; }

  .contact-band {
    position: absolute; left: 0; top: 248px; width: 100%; height: 92px;
    background: var(--band-black); color: var(--text-light);
  }
  .contact-item {
    position: absolute; top: 0; width: 260px; text-align: center;
    font-family: var(--sans); font-size: 19px; white-space: nowrap;
  }
  .contact-item .icon { display: block; margin: -16px auto 12px; width: 32px; height: 32px; }
  .contact-item--phone { left: 0; }
  .contact-item--email { left: 220px; }
  .contact-item--web { left: 440px; }

  .address-band {
    position: absolute; left: 0; top: 340px; width: 100%; height: 60px;
    background: linear-gradient(90deg, var(--accent-blue-dark), var(--accent-blue));
    color: var(--text-light);
    font-family: var(--sans); font-size: 18px; white-space: nowrap;
    display: flex; align-items: center; padding-left: 30px;
  }
</style>
</head>
<body>
<main class="sheet">

  <section class="card card--back" aria-label="Business card back">
    <h1 class="wordmark">Veridian Law</h1>
    <p class="website">www.veridianlaw.com</p>
  </section>

  <section class="card card--front" aria-label="Business card front">
    <div class="front-brand">
      <h2 class="wordmark">Veridian Law</h2>
    </div>

    <div class="person">
      <p class="person-name">MARK HALLEN</p>
      <p class="person-title">President</p>
    </div>

    <div class="contact-band">
      <div class="contact-item contact-item--phone">
        <svg class="icon" viewBox="0 0 32 32" aria-hidden="true">
          <circle cx="16" cy="16" r="16" fill="#1d6fb0"/>
          <rect x="11" y="7.5" width="10" height="17" rx="1.8" fill="none" stroke="#fff" stroke-width="2"/>
          <circle cx="16" cy="21.5" r="1" fill="#fff"/>
        </svg>
        555-014-2290
      </div>
      <div class="contact-item contact-item--email">
        <svg class="icon" viewBox="0 0 32 32" aria-hidden="true">
          <circle cx="16" cy="16" r="16" fill="#1d6fb0"/>
          <rect x="8" y="10.5" width="16" height="11" fill="#fff"/>
          <path d="M8 10.5 L16 17 L24 10.5" fill="none" stroke="#1d6fb0" stroke-width="1.4"/>
        </svg>
        info@veridianlaw.com
      </div>
      <div class="contact-item contact-item--web">
        <svg class="icon" viewBox="0 0 32 32" aria-hidden="true">
          <circle cx="16" cy="16" r="16" fill="#1d6fb0"/>
          <circle cx="16" cy="16" r="7.5" fill="none" stroke="#fff" stroke-width="1.8"/>
          <path d="M8.5 16 H23.5 M16 8.5 C12.5 12 12.5 20 16 23.5 M16 8.5 C19.5 12 19.5 20 16 23.5" fill="none" stroke="#fff" stroke-width="1.4"/>
        </svg>
        www.veridianlaw.com
      </div>
    </div>

    <div class="address-band">VERIDIAN LAW LLC, 18 Orchard Lane, Suite 300, Easton, MA 02375</div>
  </section>

</main>
</body>
</html>
```